PRP Poster

We need a poster for a doctors room to encourage people to enquire about PRP procedure.

It needs to include "for osteoarthritis and sports injuries" and "enhancing the body's natural ability to heal".

A brochure is attached which outlines what PRP (Platelet Rich Plasma) is, in the brochure it is called DVX. DO NOT USE ANY OF THE LOGOS FROM THIS BROCHURE.

Target Market(s)

patients in an orthopaedic surgery waiting room/area
age range from teenagers till 80year olds
male= female ratio

Requirements
Must have
• single poster
eye-catching yet professional
needs to be suitable/appropriate for the waiting area of a surgeons clinic
Nice to have
• prp is a natural therapy (it is essentially the person's own blood being reinjected to a site of injury)
the "natural" aspect of the therapy needs to be emphasised

```html
<!DOCTYPE html>
<html lang="en">
<head>
<meta charset="utf-8">
<title>Heal Better – PRP Procedure Poster</title>
<link rel="stylesheet" href="https://fonts.googleapis.com/css2?family=Arimo:wght@400;500&display=swap">
<style>
  :root {
    --navy: #0b4d7e;
    --sky: #2cbcf4;
    --lime: #e4f72f;
    --white: #ffffff;
    --ring-steel: #3381aa;
    --ring-soft: #3a7ba6;
    --teal: #0f899f;
    --teal-deep: #0f6c8f;
    --dot-soft: #2d6a97;
  }
  html, body {
    margin: 0;
    padding: 0;
    width: 927px;
    height: 1200px;
    overflow: hidden;
    background: var(--navy);
  }
  .poster {
    display: block;
    width: 927px;
    height: 1200px;
    font-family: "Arimo", Arial, Helvetica, sans-serif;
  }
  .backdrop { fill: var(--navy); }
  .disc-steel { fill: var(--dot-soft); opacity: .75; }
  .disc-teal { fill: var(--teal-deep); }
  .ring-steel { fill: none; stroke: var(--ring-steel); }
  .ring-soft { fill: none; stroke: var(--ring-soft); }
  .ring-teal { fill: none; stroke: var(--teal); }
  .slash { stroke: var(--lime); stroke-linecap: round; stroke-width: 24; }
  .sky { fill: var(--sky); }
  .lime { fill: var(--lime); }
  .white { fill: var(--white); }
  .headline { font-weight: 400; }
  .tagline, .call { font-weight: 500; }
</style>
</head>
<body>
<svg class="poster" viewBox="0 0 1020 1320" preserveAspectRatio="none" role="img" aria-label="Heal Better – PRP procedure poster">
  <rect class="backdrop" width="1020" height="1320"/>

  <!-- background shapes -->
  <circle class="disc-steel" cx="20" cy="15" r="92"/>
  <circle class="ring-steel" cx="905" cy="152" r="257" stroke-width="122"/>
  <circle class="disc-teal" cx="588" cy="118" r="67" opacity=".85"/>
  <line class="slash" x1="735" y1="440" x2="1030" y2="-15"/>

  <circle class="ring-teal" cx="0" cy="925" r="238" stroke-width="122"/>
  <line class="slash" x1="5" y1="920" x2="345" y2="1310"/>

  <circle class="disc-steel" cx="388" cy="800" r="62" opacity=".6"/>
  <circle class="disc-teal" cx="793" cy="893" r="67" opacity=".9"/>
  <circle class="disc-teal" cx="703" cy="1008" r="115" opacity=".9"/>
  <circle class="disc-steel" cx="912" cy="1170" r="30" opacity=".8"/>

  <circle class="ring-soft" cx="330" cy="472" r="133" stroke-width="28"/>

  <!-- headline -->
  <text class="headline" x="33" y="558">
    <tspan class="sky" font-size="251">H</tspan><tspan class="sky" font-size="175">E</tspan><tspan class="lime" font-size="175">A</tspan><tspan class="sky" font-size="175">L</tspan>
  </text>
  <text class="headline" x="506" y="610" textLength="486" lengthAdjust="spacingAndGlyphs">
    <tspan class="sky" font-size="168">B</tspan><tspan class="sky" font-size="116">E</tspan><tspan class="lime" font-size="116">TTER</tspan>
  </text>

  <!-- tagline -->
  <text class="tagline" x="65" y="668" textLength="873" lengthAdjust="spacingAndGlyphs" font-size="37">
    <tspan class="lime" font-size="50">PRP</tspan><tspan class="lime"> PROCEDURE</tspan><tspan class="white"> IS A </tspan><tspan class="lime">NATURAL</tspan><tspan class="white"> THERAPY THAT</tspan>
  </text>
  <text class="tagline white" x="40" y="718" textLength="935" lengthAdjust="spacingAndGlyphs" font-size="37">
    ENHANCES YOUR BODY’S <tspan class="lime">NATURAL</tspan> ABILITY TO HEAL
  </text>

  <!-- call to action -->
  <text class="call" x="155" y="801" textLength="742" lengthAdjust="spacingAndGlyphs" font-size="31">
    <tspan class="white">IF YOU HAVE </tspan><tspan class="lime">OSTEOARTHRITIS</tspan><tspan class="white"> OR </tspan><tspan class="lime">SPORTS INJURIES</tspan>
  </text>
  <text class="call" x="322" y="846" textLength="671" lengthAdjust="spacingAndGlyphs" font-size="31">
    <tspan class="white" font-size="42">A</tspan><tspan class="white">SK YOUR DOCTOR ABOUT </tspan><tspan class="lime" font-size="42">PRP</tspan><tspan class="lime"> PROCEDURE</tspan>
  </text>

  <!-- sign-off -->
  <text class="headline sky" x="503" y="1242" font-size="87" textLength="410" lengthAdjust="spacingAndGlyphs">SRONGER</text>
  <text class="headline lime" x="833" y="1195" font-size="45" textLength="112" lengthAdjust="spacingAndGlyphs">HEAL</text>
</svg>
</body>
</html>
```